VELINTA Promotions - Business Card Design Project

We are looking for a classy business cards for Promotion Company based in Toronto, Canada named Velinta Promotions.

Velinta Promotions has an idea and vision to set high standard, be EXCLUSIVE and attract a group of people that will follow us through events we promote (night clubs, brand promotions, music events, and sport events)

We want to present a high standards and classy image to the others...
Updates

Target Market(s)

male/female age 25-40 Target: business owners young entrepreneur - clubing industry - media industry - promotion industry - marketing media industry

Industry/Entity Type

Events

Requirements
Must have
• business cards should be classy, make people feel exclusive , make people react ..

```html
<!DOCTYPE html>
<html lang="en">
<head>
<meta charset="utf-8">
<title>Velinta Promotions – Business Cards</title>
<link rel="stylesheet" href="https://fonts.googleapis.com/css2?family=Ubuntu:wght@400;500&display=swap">
<style>
  :root {
    --page-bg: #ffffff;
    --card-front: #ffffff;
    --card-back: #000000;
    --teal-bright: #3cb7cf;
    --teal-deep: #2e8c9c;
    --ink: #1a1a1a;
    --swirl-grey: #3a3a3a;
    --shadow: rgba(0, 0, 0, 0.22);
  }
  * { margin: 0; padding: 0; box-sizing: border-box; }
  html, body {
    width: 1200px;
    height: 955px;
    overflow: hidden;
    background: var(--page-bg);
    font-family: "Ubuntu", Arial, sans-serif;
  }
  .canvas {
    position: relative;
    width: 1200px;
    height: 955px;
  }
  .card {
    position: absolute;
    width: 500px;
    height: 306px;
    border-radius: 26px;
    box-shadow: 0 10px 22px var(--shadow);
    overflow: hidden;
  }
  .card--back {
    left: 489px;
    top: 437px;
    background: var(--card-back);
    z-index: 1;
  }
  .card--front {
    left: 208px;
    top: 208px;
    background: var(--card-front);
    z-index: 2;
  }
  .brand-name {
    position: absolute;
    font-weight: 400;
    white-space: nowrap;
    letter-spacing: 0.5px;
  }
  .card--front .brand-name {
    left: 27px;
    top: 52px;
    font-size: 24px;
    color: var(--teal-bright);
  }
  .card--back .brand-name {
    left: 0;
    width: 100%;
    text-align: center;
    top: 134px;
    font-size: 34px;
    color: var(--teal-deep);
  }
  .contact {
    position: absolute;
    left: 245px;
    top: 126px;
    color: var(--ink);
  }
  .contact__name {
    font-size: 20px;
    color: var(--teal-bright);
    line-height: 22px;
  }
  .contact__role {
    font-size: 12px;
    line-height: 16px;
    margin-bottom: 14px;
  }
  .contact__address {
    font-size: 13.5px;
    line-height: 18px;
    margin-bottom: 8px;
  }
  .contact__line {
    font-size: 13.5px;
    line-height: 18px;
  }
  .contact__label {
    display: inline-block;
    width: 17px;
    font-weight: 500;
    color: var(--teal-bright);
  }
  .contact__web {
    font-size: 13.5px;
    line-height: 18px;
    margin-top: 5px;
  }
  .ornament {
    position: absolute;
  }
  .ornament--top-right {
    right: 0;
    top: 0;
    width: 90px;
    height: 120px;
    background: radial-gradient(ellipse at 70% 30%, var(--swirl-grey) 0%, rgba(58,58,58,0) 70%);
  }
  .ornament--bottom-left {
    left: 0;
    bottom: 0;
    width: 135px;
    height: 150px;
    background: radial-gradient(ellipse at 35% 70%, var(--swirl-grey) 0%, rgba(58,58,58,0) 70%);
  }
</style>
</head>
<body>
<main class="canvas">
  <section class="card card--back" aria-label="Business card back">
    <div class="ornament ornament--top-right" role="img" aria-label="Faint grey flourish swirls in the corner"></div>
    <div class="ornament ornament--bottom-left" role="img" aria-label="Faint grey flourish swirls in the corner"></div>
    <p class="brand-name">VELINTA Promotions</p>
  </section>

  <section class="card card--front" aria-label="Business card front">
    <p class="brand-name">VELINTA Promotions</p>
    <div class="contact">
      <p class="contact__name">Marcus Hale</p>
      <p class="contact__role">Managing Director</p>
      <p class="contact__address">27 Harbour Lane, Suite 4B,<br>Toronto, Ontario M5J 2N8</p>
      <p class="contact__line"><span class="contact__label">T</span>000-000 0000</p>
      <p class="contact__line"><span class="contact__label">E</span>marcus@velintapromotions.com</p>
      <p class="contact__web">www.velintapromotions.com</p>
    </div>
  </section>
</main>
</body>
</html>
```